business card for a shoe shop

we would like a business card for a family owned shoe shop.
With this information included.
Darnell's Shoe Store
Family owned since 1947

then on other side
Darnell's Shoe Store
Footwear fitting specialist
Phone: 9187 2630
218 Quarry St, Fernleigh Downs 3187
(cnr. Hartwick Rd and Quarry St)
darnellshoes218@examplemail.com
if could incorporate the purple color on card i have attached.

```html
<!DOCTYPE html>
<html lang="en">
<head>
<meta charset="utf-8">
<title>Darnell's Shoe Store – Business Card</title>
<link rel="stylesheet" href="https://fonts.googleapis.com/css2?family=Alfa+Slab+One&family=Oswald:wght@400;700&display=swap">
<style>
  :root {
    --backdrop: #d6d6d6;
    --purple: #5f52ab;
    --purple-ornament: #6c61b3;
    --silver: #a9a9ab;
    --silver-soft: #ececee;
    --card-white: #ffffff;
  }
  * { box-sizing: border-box; margin: 0; padding: 0; }
  html, body { width: 1200px; height: 848px; overflow: hidden; }
  body {
    background: var(--backdrop);
    position: relative;
    font-family: "Oswald", sans-serif;
  }
  .card {
    position: absolute;
    top: 269px;
    width: 530px;
    height: 310px;
    overflow: hidden;
  }
  .card--front { left: 55px; background: var(--purple); }
  .card--back { left: 615px; background: var(--card-white); }

  .ornament { position: absolute; border-radius: 20px; }
  .card--front .ornament { background: var(--purple-ornament); }
  .front-ornament-top { left: 150px; top: 24px; width: 230px; height: 26px; }
  .front-ornament-bottom { left: 170px; top: 260px; width: 190px; height: 24px; }

  .front-frame {
    position: absolute; left: 50px; top: 62px; width: 430px; height: 186px;
    border: 4px solid var(--silver);
  }
  .front-lockup {
    position: absolute; left: 54px; top: 66px; width: 422px; height: 178px;
    display: flex; flex-direction: column; align-items: center; justify-content: center;
    gap: 10px;
  }
  .brand-row { display: flex; align-items: center; gap: 12px; }
  .brand-dot {
    flex: none;
    width: 30px; height: 30px; border-radius: 50%;
    border: 2px solid var(--silver);
  }
  .brand-name {
    font-family: "Alfa Slab One", serif;
    color: var(--silver);
    font-weight: 400;
    font-size: 27px;
    letter-spacing: 0.5px;
    white-space: nowrap;
  }
  .tagline {
    font-family: "Oswald", sans-serif;
    font-weight: 700;
    text-transform: uppercase;
    color: var(--silver);
    letter-spacing: 1.5px;
    white-space: nowrap;
  }
  .card--front .tagline {
    font-size: 15px;
    border-top: 2px solid var(--silver);
    padding-top: 6px;
  }

  .back-frame {
    position: absolute; inset: 14px;
    border: 2px solid var(--silver);
  }
  .card--back .ornament { background: var(--silver-soft); }
  .back-ornament { right: 40px; top: 34px; width: 90px; height: 60px; border-radius: 30px; }
  .back-header {
    position: absolute; left: 40px; top: 32px;
    display: flex; flex-direction: column; gap: 4px;
  }
  .card--back .brand-name { font-size: 27px; }
  .card--back .tagline { font-size: 13px; }
  .contact-icons {
    position: absolute; left: 40px; top: 128px;
    display: flex; gap: 18px;
  }
  .contact-icon {
    width: 38px; height: 38px; border-radius: 50%;
    border: 2px solid var(--silver);
    display: flex; align-items: center; justify-content: center;
  }
  .contact-icon svg { width: 20px; height: 20px; fill: var(--silver); }
  .contact-details {
    position: absolute; left: 40px; top: 180px;
    color: var(--silver);
    font-size: 15px; line-height: 1.45;
    list-style: none;
  }
  .contact-label { font-weight: 700; text-transform: uppercase; letter-spacing: 0.5px; }
</style>
</head>
<body>

<section class="card card--front" aria-label="Business card front">
  <div class="ornament front-ornament-top" role="img" aria-label="Decorative scroll flourish"></div>
  <div class="front-frame"></div>
  <div class="front-lockup">
    <div class="brand-row">
      <span class="brand-dot"></span>
      <span class="brand-name">Darnell's Shoe Store</span>
    </div>
    <p class="tagline">Family owned since 1947</p>
  </div>
  <div class="ornament front-ornament-bottom" role="img" aria-label="Decorative scroll flourish"></div>
</section>

<section class="card card--back" aria-label="Business card back">
  <div class="back-frame"></div>
  <div class="ornament back-ornament" role="img" aria-label="Decorative scroll flourish"></div>
  <header class="back-header">
    <span class="brand-name">Darnell's Shoe Store</span>
    <p class="tagline">Footwear fitting specialist</p>
  </header>

  <div class="contact-icons">
    <span class="contact-icon" aria-label="Phone">
      <svg viewBox="0 0 24 24"><path d="M6.6 10.8a15.1 15.1 0 0 0 6.6 6.6l2.2-2.2a1 1 0 0 1 1-.25 11.4 11.4 0 0 0 3.6.57 1 1 0 0 1 1 1V20a1 1 0 0 1-1 1A17 17 0 0 1 3 4a1 1 0 0 1 1-1h3.5a1 1 0 0 1 1 1c0 1.250.2 2.450.57 3.57a1 1 0 0 1-.25 1z"/></svg>
    </span>
    <span class="contact-icon" aria-label="Address">
      <svg viewBox="0 0 24 24"><path d="M12 2a7 7 0 0 0-7 7c0 5.2 7 13 7 13s7-7.8 7-13a7 7 0 0 0-7-7zm0 9.5A2.5 2.5 0 1 1 12 6.5a2.5 2.5 0 0 1 0 5z"/></svg>
    </span>
    <span class="contact-icon" aria-label="Email">
      <svg viewBox="0 0 24 24"><path d="M3 5h18v14H3z M3 5l9 7 9-7" fill="none" stroke="#a9a9ab" stroke-width="2" stroke-linejoin="round"/></svg>
    </span>
  </div>

  <ul class="contact-details">
    <li><span class="contact-label">Phone:</span> 9187 2630</li>
    <li><span class="contact-label">Address:</span> 218 Quarry St, Fernleigh Downs 3187</li>
    <li>(cnr. Hartwick Rd and Quarry St)</li>
    <li>darnellshoes218@examplemail.com</li>
  </ul>
</section>

</body>
</html>
```